Maison Corvel

I am actually making my own traditional french food.
Everything is homemade with passion.
I make differente terrines, jams, macaroons, rillettes and much more
I do as well cocktail party and catering
Updates

Hello everyone,

On the business card I would like to see appear if it's possible these following informations: traditional french food, cocktail party and catering.

Industry/Entity Type

Catering

```html
<!DOCTYPE html>
<html lang="en">
<head>
<meta charset="utf-8">
<title>Maison Corvel – Business Card</title>
<link rel="stylesheet" href="https://fonts.googleapis.com/css2?family=Questrial&family=Nunito+Sans:wght@400;800&display=swap">
<style>
  :root {
    --page: #ffffff;
    --wine: #a31c25;
    --wine-dark: #8e1a20;
    --wine-stripe: #981922;
    --navy: #2b2f9e;
    --paper: #ffffff;
    --paper-stripe: #ececec;
    --white: #ffffff;
  }
  html, body {
    margin: 0;
    padding: 0;
    width: 1200px;
    height: 848px;
    overflow: hidden;
    background: var(--page);
  }
  .sheet {
    position: relative;
    width: 1200px;
    height: 848px;
    font-family: "Questrial", "Century Gothic", sans-serif;
  }
  .card {
    position: absolute;
    top: 282px;
    width: 495px;
    height: 276px;
    box-sizing: border-box;
  }
  .card--front {
    left: 44px;
    background: repeating-linear-gradient(90deg, var(--wine) 0 9px, var(--wine-stripe) 9px 18px);
    border: 1px solid var(--wine-dark);
  }
  .card--back {
    left: 638px;
    background: repeating-linear-gradient(90deg, var(--paper) 0 9px, var(--paper-stripe) 9px 18px);
    border: 7px solid var(--wine-dark);
  }
  .brand {
    position: absolute;
    display: flex;
    align-items: center;
    gap: 12px;
    font-size: 22px;
  }
  .card--front .brand {
    left: 0;
    right: 0;
    top: 76px;
    justify-content: center;
    color: var(--white);
  }
  .brand__dot {
    width: 40px;
    height: 40px;
    border-radius: 50%;
    background: var(--white);
    flex: none;
  }
  .card--back .brand {
    left: 12px;
    top: 46px;
    width: 160px;
    flex-direction: column;
    gap: 10px;
    color: var(--wine-dark);
    font-size: 19px;
  }
  .card--back .brand__dot {
    width: 90px;
    height: 90px;
    background: var(--wine-dark);
  }
  .services {
    position: absolute;
    left: 0;
    right: 0;
    text-align: center;
    font-size: 13.5px;
    margin: 0;
  }
  .card--front .services { top: 228px; color: var(--white); }
  .card--back .services { top: 227px; left: 40px; color: var(--navy); font-size: 14.5px; }
  .contact {
    position: absolute;
    left: 194px;
    top: 36px;
    color: var(--wine-dark);
  }
  .contact__name { margin: 0; font-size: 22px; font-weight: 400; line-height: 1.1; }
  .contact__role {
    margin: 0 0 12px;
    font-family: "Nunito Sans", Arial, sans-serif;
    font-weight: 800;
    font-size: 15px;
    color: var(--navy);
  }
  .contact__line {
    display: flex;
    align-items: center;
    gap: 8px;
    margin: 0 0 6px;
  }
  .contact__line--phone { font-size: 23px; }
  .contact__line--mail { font-size: 18px; }
  .contact__icon { flex: none; }
</style>
</head>
<body>
<main class="sheet">
  <section class="card card--front" aria-label="Card front">
    <div class="brand"><span class="brand__dot"></span><span class="brand__name">Maison Corvel</span></div>
    <p class="services">Traditional french food • Cocktail party • Catering</p>
  </section>

  <section class="card card--back" aria-label="Card back">
    <div class="brand"><span class="brand__dot"></span><span class="brand__name">Maison Corvel</span></div>
    <div class="contact">
      <h1 class="contact__name">Julien Perrault</h1>
      <p class="contact__role">Owner</p>
      <p class="contact__line contact__line--phone">
        <svg class="contact__icon" width="14" height="18" viewBox="0 0 14 18" aria-hidden="true">
          <path d="M3 1 L6 1 L6.5 5 L4.5 6.5 C5 9.5 6.5 11.5 8.5 12.5 L10 10.5 L13 11.5 L13 15 C12 17 9 17 6 14.5 C2.5 11.5 1 7 1.5 3.5 Z" fill="#333"/>
        </svg>
        <span>0412557019</span>
      </p>
      <p class="contact__line contact__line--mail">
        <svg class="contact__icon" width="16" height="12" viewBox="0 0 16 12" aria-hidden="true">
          <rect x="1" y="1" width="14" height="10" fill="none" stroke="#333" stroke-width="1.6"/>
          <path d="M1 1 L8 7 L15 1" fill="none" stroke="#333" stroke-width="1.6"/>
        </svg>
        <span>julien.p@corvel.fr</span>
      </p>
    </div>
    <p class="services">Traditional french food • Cocktail party • Catering</p>
  </section>
</main>
</body>
</html>
```